DPW Business Card

This is a wide-range political consulting firm specializing in high-profile political campaigns. Red should be a predominant color in the business card, since this is a Lantern Party inspired consulting firm, but the word "lantern" will not appear anywhere in any kind of literature. Look has to be clean and crisp. The design should be forward thinking and appropriate for a company that is trying to break away from a traditionally "stodgy" image in politics.

Target Market(s)

potential national political candidates, wealthy donors,

Industry/Entity Type

Political

Contact Information for Business Card

Doran P. Whitcliffe
Political Consultant
437 Orchard Lane SE
#358
Washington, DC 20417

```html
<!DOCTYPE html>
<html lang="en">
<head>
<meta charset="utf-8">
<title>DPW Business Card</title>
<link rel="stylesheet" href="https://fonts.googleapis.com/css2?family=Arimo:wght@400;700&family=Open+Sans:wght@400&display=swap">
<style>
  :root {
    --page-bg: #ebe7e1;
    --card-center: #cc2a29;
    --card-mid: #b4211f;
    --card-edge: #8c181c;
    --divider-dark: rgba(90, 8, 12, 0.55);
    --divider-light: rgba(255, 120, 110, 0.18);
    --name-light: #ffffff;
    --name-silver: #c9c9cc;
    --title-ink: #5e1013;
    --address-ink: #ffffff;
  }
  html, body {
    margin: 0;
    padding: 0;
    width: 1200px;
    height: 970px;
    overflow: hidden;
    background: var(--page-bg);
  }
  .business-card {
    position: absolute;
    left: 131px;
    top: 215px;
    width: 938px;
    height: 540px;
    background: radial-gradient(ellipse 620px 420px at 610px 185px, var(--card-center) 0%, var(--card-mid) 45%, var(--card-edge) 100%);
    box-shadow: 0 4px 10px rgba(0, 0, 0, 0.18);
  }
  .divider {
    position: absolute;
    left: 466px;
    top: 135px;
    width: 2px;
    height: 280px;
    background: linear-gradient(to bottom, transparent, var(--divider-dark) 25%, var(--divider-dark) 75%, transparent);
    box-shadow: 1px 0 0 var(--divider-light);
  }
  .identity {
    position: absolute;
    right: 491px;
    text-align: right;
  }
  .name {
    position: absolute;
    right: 0;
    top: 253px;
    margin: 0;
    white-space: nowrap;
    font-family: "Arimo", Arial, sans-serif;
    font-weight: 700;
    font-size: 37px;
    line-height: 1;
    letter-spacing: 0.2px;
    background: linear-gradient(to bottom, var(--name-light) 30%, var(--name-silver) 100%);
    -webkit-background-clip: text;
    background-clip: text;
    color: transparent;
    filter: drop-shadow(1px 2px 1px rgba(60, 0, 0, 0.6));
  }
  .role {
    position: absolute;
    right: 2px;
    top: 305px;
    margin: 0;
    white-space: nowrap;
    font-family: "Open Sans", Arial, sans-serif;
    font-weight: 400;
    font-size: 17px;
    line-height: 1;
    color: var(--title-ink);
  }
  .address {
    position: absolute;
    left: 517px;
    top: 227px;
    margin: 0;
    font-family: "Arimo", Arial, sans-serif;
    font-style: normal;
    font-weight: 400;
    font-size: 27px;
    line-height: 40px;
    color: var(--address-ink);
    white-space: nowrap;
  }
</style>
</head>
<body>
  <div class="business-card">
    <div class="identity">
      <h1 class="name">DORAN P. WHITCLIFFE</h1>
      <p class="role">POLITICAL CONSULTANT</p>
    </div>
    <div class="divider"></div>
    <address class="address">437 ORCHARD LANE<br>SE #358 WASHINGTON,<br>DC 20417</address>
  </div>
</body>
</html>
```